Horse related business entrepreneur needs a business card

I need a business card design for my horse related business. The enterprise is Copper Vale LLC and I have 3 businesses (headquartered at 2 locations): 1. property management where we rent horse stalls and apartments at a thoroughbred training center outside Ocala; 2. a medium sized transportation service in central Florida that sells horse bedding and removes used horse bedding from horse farms; and horse racing

```html
<!DOCTYPE html>
<html lang="en">
<head>
<meta charset="utf-8">
<title>Copper Vale LLC – Business Card</title>
<link href="https://fonts.googleapis.com/css2?family=Michroma&family=Roboto:wght@400;700&display=swap" rel="stylesheet">
<style>
  :root {
    --backdrop: #2a2a2b;
    --card-black: #0c0c0d;
    --card-black-hi: #2b2b2e;
    --card-white: #ffffff;
    --brand-red: #d8352b;
    --brand-orange: #ec5a33;
    --ink-dark: #1d1d1f;
    --ink-grey: #5d5860;
    --rule-white: #e9e9e9;
  }
  * { box-sizing: border-box; margin: 0; padding: 0; }
  html, body {
    width: 1200px; height: 902px; overflow: hidden;
    background: var(--backdrop);
    font-family: "Roboto", Arial, sans-serif;
  }
  .sheet {
    width: 1200px; height: 902px;
    display: flex; flex-direction: column; align-items: center; justify-content: center;
    gap: 60px;
  }
  .card {
    position: relative;
    width: 600px; height: 343px;
    border-radius: 22px;
    overflow: hidden;
    box-shadow: 0 10px 28px rgba(0,0,0,.45);
  }

  /* Back side */
  .card-back {
    background: linear-gradient(160deg, var(--card-black-hi) 0%, var(--card-black) 45%);
  }
  .card-back .brand {
    position: absolute; left: 0; right: 0; top: 52px;
    display: flex; flex-direction: column; align-items: center; gap: 22px;
  }
  .brand-dot {
    width: 110px; height: 110px; border-radius: 50%;
    background: radial-gradient(circle at 40% 35%, var(--brand-orange), var(--brand-red));
  }
  .brand-name {
    font-family: "Michroma", "Arial Black", sans-serif;
    font-size: 28px; letter-spacing: 1px; color: #ffffff;
    white-space: nowrap;
  }
  .card-back .address-band {
    position: absolute; left: 0; right: 0; bottom: 0; height: 92px;
    background: linear-gradient(90deg, var(--brand-red), var(--brand-orange));
    border-top: 5px solid var(--rule-white);
    display: flex; flex-direction: column; align-items: center; justify-content: center;
    gap: 6px;
    color: #ffffff; font-size: 15px; letter-spacing: .3px;
  }

  /* Front side */
  .card-front { background: var(--card-white); }
  .card-front .brand-name {
    position: absolute; left: 34px; top: 92px;
    font-size: 19px; letter-spacing: .5px; color: var(--ink-dark);
  }
  .card-front .brand-dot {
    position: absolute; right: 30px; top: 52px;
    width: 240px; height: 240px;
  }
  .holder { position: absolute; left: 34px; top: 192px; }
  .holder-name {
    font-family: "Michroma", "Arial Black", sans-serif;
    font-size: 19px; color: var(--ink-dark);
  }
  .holder-role {
    font-family: "Michroma", "Arial Black", sans-serif;
    font-size: 13px; color: var(--brand-red); margin-top: 2px;
  }
  .contact-list { list-style: none; margin-top: 10px; }
  .contact-list li {
    display: flex; align-items: center; gap: 10px;
    font-size: 16px; color: var(--ink-dark); height: 24px;
  }
  .contact-list svg { width: 16px; height: 16px; fill: var(--brand-red); flex: none; }
  .contact-list .no-icon { width: 16px; flex: none; }
</style>
</head>
<body>
<main class="sheet">

  <section class="card card-back">
    <div class="brand">
      <div class="brand-dot"></div>
      <div class="brand-name">COPPER VALE LLC</div>
    </div>
    <div class="address-band">
      <p>1200 SE Meadow Lane, Oakfield, FL 32000</p>
      <p>85 Birch Hollow Road, Fairmont, VA 22000</p>
    </div>
  </section>

  <section class="card card-front">
    <div class="brand-name">COPPER VALE LLC</div>
    <div class="brand-dot"></div>
    <div class="holder">
      <div class="holder-name">DALE MORROW</div>
      <div class="holder-role">OWNER</div>
      <ul class="contact-list">
        <li><span class="no-icon"></span>(555) 014-7051</li>
        <li>
          <svg viewBox="0 0 24 24" aria-hidden="true"><path d="M6.6 10.8a15.1 15.1 0 0 0 6.6 6.6l2.2-2.2a1 1 0 0 1 1-.25 11.4 11.4 0 0 0 3.6.57 1 1 0 0 1 1 1V20a1 1 0 0 1-1 1A17 17 0 0 1 3 4a1 1 0 0 1 1-1h3.5a1 1 0 0 1 1 1c0 1.250.2 2.450.57 3.57a1 1 0 0 1-.25 1z"/></svg>
          (555) 018-0402
        </li>
        <li>
          <svg viewBox="0 0 24 24" aria-hidden="true"><path d="M2 5h20v14H2z M3.5 6.5 12 13l8.5-6.5" stroke="#fff" stroke-width="1.4"/></svg>
          dale@coppervale.com
        </li>
      </ul>
    </div>
  </section>

</main>
</body>
</html>
```